Rapidly Expanding Real Estate Firm Seeking Signage Designs for Multiple Properties

We would like a sign design template created that we can use at our apartment buildings. We would like a consistent sign appearance that is adaptable enough to be used at different locations, on different mediums, and in different sizes. All vary for signage depending on the local laws and regulations as well as the type and style of the property. But the sign design should be consistent enough to support our company's branding efforts; so people that see our sign know its our company but also that the specific property is unique. Our thought was to incorporate the property address; i.e. "418 Larkwood" along with a portion of our company logo(attached). Then tag our website address across the bottom. Or some combination of that structure/design. It may make sense to just use the address and website address across the bottom OR it might be good to say 418 Larkwood St in large font with "by Amber Ridge Holdings Group" underneath as sort of a tag line. Not quite sure.
But we definitely want the signage to be clearly visible, professional, and clean. Easily read for the street. Should be flexible enough to work on metal or wood or any other medium with updates for the address and maybe color.
This is not a for sale sign design request. The sign concept will be used at apartment buildings. Sample property photos are attached - we are looking for a design template that is flexible enough to work on various property types. Also could be wall mounted or a pylon sign. Concept should work either way.

Target Market(s)

Prospective Tenants 25-45 yrs of age with incomes ranging from $55k - $95k.

Industry/Entity Type

Real Estate - Apartments

Colors
59FF00
82FF00
B8FF75
E3FFCB
F4FFEA

Requirements
Must have
• The street address number, web address(www.amberridgeholdingsgroup.example), & incorporate our primary colors(green,white,black)
Nice to have
• "418 Larkwood St." by Amber Ridge
Should not have
• Should not say For Sale, For Lease, post our phone number.

```html
<!DOCTYPE html>
<html lang="en">
<head>
<meta charset="utf-8">
<title>418 Larkwood St – Property Sign</title>
<link href="https://fonts.googleapis.com/css2?family=Exo+2:wght@400;500;700;800;900&display=swap" rel="stylesheet">
<style>
  :root {
    --brand-green: #88c343;
    --brand-gray: #a7a9ac;
    --white: #ffffff;
    --backdrop: #e6e6e6;
  }
  * { margin: 0; padding: 0; box-sizing: border-box; }
  html, body {
    width: 1076px;
    height: 1200px;
    overflow: hidden;
    background: var(--backdrop);
    font-family: "Exo 2", sans-serif;
  }
  .sign {
    position: absolute;
    left: 93px;
    top: 43px;
    width: 890px;
    height: 1113px;
    background: var(--white);
  }
  .sign-frame {
    position: absolute;
    left: 25px;
    top: 26px;
    width: 839px;
    height: 1061px;
    border: 3px solid var(--brand-green);
  }
  .company-name {
    position: absolute;
    left: 0;
    right: 0;
    top: 250px;
    text-align: center;
    font-weight: 800;
    text-transform: uppercase;
    line-height: 1.05;
  }
  .company-name .line-main {
    display: block;
    font-size: 66px;
    letter-spacing: 4px;
    color: var(--brand-green);
  }
  .company-name .line-sub {
    display: block;
    font-size: 34px;
    letter-spacing: 4px;
    margin-top: 6px;
    color: var(--brand-gray);
  }
  .web-address {
    position: absolute;
    left: 0;
    right: 0;
    top: 636px;
    text-align: center;
    font-weight: 800;
    font-size: 35px;
    letter-spacing: 1px;
    color: var(--brand-green);
  }
  .web-address .tld { color: var(--brand-gray); }
  .address-band {
    position: absolute;
    left: 25px;
    top: 843px;
    width: 839px;
    height: 244px;
    background: var(--brand-green);
    color: var(--white);
    text-align: center;
  }
  .property-address {
    margin-top: 38px;
    font-weight: 900;
    font-size: 92px;
    line-height: 1;
    letter-spacing: 1px;
  }
  .property-tagline {
    margin-top: 18px;
    font-weight: 400;
    font-size: 40px;
    letter-spacing: 1px;
    line-height: 1;
  }
</style>
</head>
<body>
  <div class="sign">
    <div class="sign-frame"></div>

    <div class="company-name">
      <span class="line-main">Amber Ridge</span>
      <span class="line-sub">Holdings Group LLC</span>
    </div>

    <div class="web-address">amberridgeholdingsgroup<span class="tld">.example</span></div>

    <div class="address-band">
      <div class="property-address">418 Larkwood St</div>
      <div class="property-tagline">by Amber Ridge Holdings Group</div>
    </div>
  </div>
</body>
</html>
```